Webdesign for large cottage directory

We have developed a first version of a website that can accommodate large groups (10 to 300 people). The site is English and is aimed at a wide audience ranging from a group of students to a family or a family. For the visitors the site is free and it is the propietaires who pay to see their accommodation. The site is online with just a few fake lodgings and a simple design to the elements that must be appraised (nothing to keep the current design). Our website is here: lodgevista.com (login / pass = admin / 123) Home page (lodgevista.com): on this page section) and lodging by theme (third section). These three points should be highlighted as possible. The displayed map may be slightly modified. Only the background and the color changes when hovering over the mouse. It can be enlarged / retreciated. Below these 3 sections we have some fairly published articles, the latest blog posts and the footer. The menu will be visible throughout the site. Category page (https://lodgevista.fr/gite-departement/aveyron OR https://lodgevista.fr/gites-couchages-121): On these pages we always return the same format with the googlemap, an image 1 text. Below the list of the cottages concerned and the filter options. Product page: The pages presenting the cottages can be of two types: - Either the cottage has no owner and there is no contact for the visitor to the owner that he can retrieve his cottage by registering: example of a page of this type: https://lodgevista.fr/domaine-de-fressanac - The cottage to a propietaire and we are on the classic card. : // lodgevista. en / domain-of-fressanac2 For all products on the site we have nav tab. It's just for testing. We do not want to be in the design for real website. All information must be in the page without login / register page: classic, it's here: https://lodgevista.it/login and https://lodgevista.fr/register Blog homepage (https://lodgevista.fr/blog ): Classic blog page Blog post (https://lodgevista.fr/blog/urltemporaire1551521154) and static page (https://lodgevista.fr/blog/Systeme-classement-lodgevistafr): Nothing special Menu: Menu is an important part of the website. It's the way to navigate on the wbesite.
Faible participation designers
Number of Pages Required
4 page
Colors
Designer to choose colors to be used in the design.
Look and feel
Each slider illustrates characteristics of the customer's brand and the style your logo design should communicate.

```html
<!DOCTYPE html>
<html lang="en">
<head>
<meta charset="utf-8">
<title>lodgevista.fr — Group lodging directory</title>
<link href="https://fonts.googleapis.com/css2?family=Raleway:wght@300;400;600;800&family=Open+Sans:wght@400;600;700&display=swap" rel="stylesheet">
<style>
:root{
  --brand:#cc0b5c;
  --brand-dark:#a8064a;
  --ink:#222;
  --muted:#666;
  --light:#efefef;
  --pale:#f5f5f5;
  --ad:#c9c9c9;
  --footer:#262626;
  --footer-base:#1b1b1b;
  --white:#fff;
}
*{box-sizing:border-box;margin:0;padding:0}
html,body{width:1200px;height:3740px;overflow:hidden}
body{font-family:"Open Sans",Arial,sans-serif;color:var(--ink);background:var(--white);position:relative}
.abs{position:absolute}

/* top bar */
.topbar{position:absolute;top:0;left:0;width:1200px;height:31px;background:var(--white);border-bottom:1px solid #eee;font-size:11px;color:var(--muted)}
.topbar span{position:absolute;top:9px;display:flex;align-items:center;gap:5px;white-space:nowrap}
.topbar svg{width:10px;height:10px;fill:var(--brand)}

/* nav */
.nav{position:absolute;top:31px;left:0;width:1200px;height:53px;background:var(--white)}
.logo{position:absolute;left:171px;top:12px;font-weight:700;font-size:24px;color:var(--ink)}
.menu{position:absolute;right:171px;top:0;display:flex;gap:30px;height:53px;align-items:center;font-size:13px;font-weight:700;text-transform:uppercase}
.menu a{color:var(--ink);text-decoration:none;padding:17px 0}
.menu a.active{color:var(--brand);border-bottom:3px solid var(--brand)}

/* hero */
.hero{position:absolute;top:84px;left:0;width:1200px;height:493px;background:linear-gradient(180deg,#4d5b2e 0%,#6f5a3a 35%,#8a4a3a 60%,#3c3b27 100%)}
.hero-shade{position:absolute;inset:0;background:rgba(0,0,0,.22)}
.hero-title{position:absolute;top:170px;width:1200px;text-align:center;font-family:"Raleway",sans-serif;font-weight:800;font-size:52px;letter-spacing:3px;color:var(--white)}
.hero-arrow{position:absolute;top:190px;width:26px;height:26px}
.capacity{position:absolute;left:175px;top:346px;width:854px;height:147px;background:var(--brand);padding:0 13px}
.capacity h3{font-family:"Raleway",sans-serif;font-weight:600;font-size:17px;color:var(--white);margin-top:12px;display:flex;align-items:center;gap:9px}
.cap-row{display:flex;gap:22px;margin-top:12px}
.cap-item{width:120px;text-align:center}
.cap-box{height:52px;background:var(--white);display:flex;align-items:center;justify-content:center;font-size:21px;font-weight:600;color:var(--ink)}
.cap-label{font-size:10px;color:var(--white);margin-top:9px;white-space:nowrap}

/* welcome */
.welcome{position:absolute;top:577px;left:0;width:1200px;height:411px;background:var(--light)}
.welcome-text{position:absolute;left:172px;top:70px;width:490px}
.welcome h2{font-family:"Raleway",sans-serif;font-weight:400;font-size:34px;line-height:42px;color:#333}
.welcome .sub{font-size:15px;text-decoration:underline;color:#333;margin-top:6px}
.welcome p{font-size:12px;line-height:19px;color:var(--muted);margin-top:14px}
.btn{display:inline-flex;align-items:center;justify-content:center;background:var(--brand);color:var(--white);font-size:10px;font-weight:700;text-transform:uppercase;letter-spacing:.5px}
.welcome .btn{width:140px;height:29px;margin-top:20px}
.welcome-photo{position:absolute;left:686px;top:78px;width:305px;height:255px;background:linear-gradient(180deg,#c6d3dc 0%,#d69a77 40%,#8b8f7a 75%,#6a6656 100%);border:5px solid var(--white);box-shadow:0 4px 14px rgba(0,0,0,.25)}

/* department */
.department{position:absolute;top:988px;left:0;width:1200px;height:624px;background:linear-gradient(180deg,#5e6b72 0%,#3e4a44 40%,#2b3a2a 70%,#1d2620 100%)}
.section-title-light{position:absolute;top:40px;width:1200px;text-align:center;font-family:"Raleway",sans-serif;font-weight:400;font-size:36px;color:var(--white)}
.map-card{position:absolute;left:165px;top:125px;width:437px;height:439px;background:var(--white);padding:18px}
.map-area{width:100%;height:100%;background:linear-gradient(160deg,#e7e4df,#dcd8d2)}
.dept-info{position:absolute;left:655px;top:270px;width:330px;color:var(--white)}
.dept-info .name{font-size:17px;font-weight:700;color:var(--brand)}
.dept-info .kind{font-size:13px;font-weight:600;margin-top:4px}
.dept-info p{font-size:10.5px;line-height:16px;margin-top:8px}
.dept-info .maplink{display:flex;align-items:center;gap:9px;font-size:19px;margin-top:42px}

/* themes */
.themes{position:absolute;top:1612px;left:0;width:1200px;height:882px;background:var(--pale)}
.section-title{position:absolute;width:1200px;text-align:center;font-family:"Raleway",sans-serif;font-weight:400;font-size:36px;color:#333}
.themes .section-title{top:72px}
.themes .lead{position:absolute;top:124px;width:1200px;text-align:center;font-size:14px;font-weight:600;color:var(--muted)}
.theme-grid{position:absolute;left:172px;top:199px;width:857px;display:grid;grid-template-columns:repeat(4,206px);grid-auto-rows:200px;gap:17px 11px}
.theme-tile{position:relative;display:flex;align-items:center;justify-content:center;text-align:center;color:var(--white);font-weight:700;font-size:17px;line-height:21px;text-shadow:0 1px 3px rgba(0,0,0,.6);padding:10px}
.t1{background:linear-gradient(160deg,#4a4a4a,#8a7c6c)}
.t2{background:linear-gradient(180deg,#c37a4e,#3b2a29)}
.t3{background:linear-gradient(180deg,#c8d0d8,#6a4a44)}
.t4{background:linear-gradient(180deg,#1f4a66,#0f2435)}
.t5{background:linear-gradient(160deg,#5d5b46,#2e2820)}
.t6{background:linear-gradient(160deg,#7a3f2c,#3b2a20)}
.t7{background:linear-gradient(180deg,#9aa1a8,#4f565d)}
.t8{background:linear-gradient(180deg,#d79449,#2e2a2c)}
.t9{background:linear-gradient(160deg,#b07a3c,#5c3d6a)}
.t10{background:linear-gradient(180deg,#4a6b88,#7a5a4a)}
.t11{background:linear-gradient(180deg,#8fa0ad,#4d5a38)}
.t12{background:linear-gradient(160deg,#2c2620,#7a4a2a)}

/* ads */
.ads{position:absolute;top:2494px;left:0;width:1200px;height:349px}
.ad{position:absolute;background:var(--ad);color:var(--white);font-size:18px;display:flex;align-items:center;justify-content:center}
.divider{position:absolute;left:172px;top:2843px;width:857px;height:1px;background:#e2e2e2}

/* blog */
.blog .section-title{top:2900px}
.post{position:absolute;top:2992px;width:266px;height:306px;background:var(--white);box-shadow:0 1px 6px rgba(0,0,0,.15)}
.post-photo{height:162px}
.post h4{font-size:13px;font-weight:700;text-align:center;margin:12px 0 0}
.post p{font-size:9.5px;line-height:14px;color:var(--muted);padding:10px 12px 0}
.post-meta{position:absolute;bottom:12px;left:12px;right:12px;display:flex;justify-content:space-between;font-size:9px;color:var(--muted);border-top:1px solid #eee;padding-top:9px}
.blog .btn{position:absolute;left:502px;top:3338px;width:196px;height:29px;font-size:10px;text-transform:none}

/* footer */
.footer{position:absolute;top:3438px;left:0;width:1200px;height:265px;background:var(--footer);color:#cfcfcf}
.footer .f-logo{position:absolute;left:172px;top:70px;font-weight:700;font-size:22px;color:var(--white)}
.footer .f-about{position:absolute;left:172px;top:106px;width:250px;font-size:10.5px;line-height:16px}
.footer h5{font-size:14px;font-weight:600;color:var(--white)}
.f-col{position:absolute;top:74px}
.f-col ul{list-style:none;margin-top:18px;font-size:10.5px;line-height:18px}
.f-col li{display:flex;gap:7px;align-items:flex-start}
.f-col .dot{width:6px;height:6px;background:var(--brand);margin-top:6px;flex:none}
.f-input{width:197px;height:32px;background:var(--white);color:#888;font-size:10px;padding:9px 10px;margin-top:22px}
.f-col .btn{width:197px;height:28px;margin-top:18px}
.copy{position:absolute;top:3703px;left:0;width:1200px;height:37px;background:var(--footer-base);color:#bdbdbd;font-size:10px;text-align:center;line-height:37px}
</style>
</head>
<body>

<header>
  <div class="topbar">
    <span style="left:560px"><svg viewBox="0 0 10 10"><path d="M2 0l2 2-1 1.5c.6 1.3 1.6 2.3 3 3L7.5 5.5 10 7.5 8.5 10C4 10 0 6 0 1.5z"/></svg>0400-5550182</span>
    <span style="left:690px"><svg viewBox="0 0 10 10"><path d="M0 2h10v6H0z"/></svg>contact@lodgevista.fr</span>
    <span style="left:842px"><svg viewBox="0 0 10 10"><circle cx="5" cy="3" r="2.5"/><path d="M0 10c0-3 2-4.5 5-4.5s5 1.5 5 4.5z"/></svg>Login / Register</span>
    <span style="left:960px"><svg viewBox="0 0 10 10"><rect x="0" y="2" width="10" height="6"/></svg>Eng ▾</span>
  </div>
  <nav class="nav">
    <div class="logo">lodgevista.fr</div>
    <div class="menu">
      <a class="active" href="#">Home</a>
      <a href="#">Your Favorites</a>
      <a href="#">Blog</a>
      <a href="#">Contact Us</a>
    </div>
  </nav>
</header>

<section class="hero">
  <div class="abs" role="img" aria-label="Photo of a group of friends sharing a meal outdoors" style="inset:0"></div>
  <div class="hero-shade"></div>
  <h1 class="hero-title">ENJOY YOUR HOLIDAYS</h1>
  <svg class="hero-arrow" style="left:124px" viewBox="0 0 26 26"><path d="M16 5l-8 8 8 8" stroke="#fff" stroke-width="3" fill="none"/></svg>
  <svg class="hero-arrow" style="left:1050px" viewBox="0 0 26 26"><path d="M10 5l8 8-8 8" stroke="#fff" stroke-width="3" fill="none"/></svg>
  <div class="capacity">
    <h3><svg width="18" height="18" viewBox="0 0 18 18"><path d="M2 8l7-6 7 6v8H2z" fill="none" stroke="#fff" stroke-width="2"/></svg>Lodging By Capacity</h3>
    <div class="cap-row">
      <div class="cap-item"><div class="cap-box">2-20</div><div class="cap-label">2 to 20 people</div></div>
      <div class="cap-item"><div class="cap-box">20-40</div><div class="cap-label">20 to 40 People</div></div>
      <div class="cap-item"><div class="cap-box">40-60</div><div class="cap-label">40 to 60 People</div></div>
      <div class="cap-item"><div class="cap-box">60-80</div><div class="cap-label">60 to 80 People</div></div>
      <div class="cap-item"><div class="cap-box">80-120</div><div class="cap-label">80 to 120 People</div></div>
      <div class="cap-item"><div class="cap-box">120+</div><div class="cap-label">More Than 120 People</div></div>
    </div>
  </div>
</section>

<section class="welcome">
  <div class="welcome-text">
    <h2>Welcome To lodgevista</h2>
    <div class="sub">High quality accommodation services</div>
    <p>Donec quis eros eget tellus varius suscipit. Duis a purus gravida, pretium lectus et, pretium enim. Maecenas tellus diam, lobortis eu lorem eget, placerat euismod arcu. Aenean aliquam metus nec sodales consequat, neque libero ornare sem, at dapibus dolor nunc et leo. Etiam gravida diam sit amet fermentum accumsan, purus diam condimentum justo, vitae venenatis metus lorem vel elit. Suspendisse ornare risus leo.</p>
    <span class="btn">Register Now</span>
  </div>
  <div class="welcome-photo" role="img" aria-label="Photo of a colourful paved village street"></div>
</section>

<section class="department">
  <div class="abs" role="img" aria-label="Photo of a river valley landscape at dusk" style="inset:0;background:rgba(0,0,0,.15)"></div>
  <h2 class="section-title-light">Lodging By Department</h2>
  <div class="map-card">
    <div class="map-area" role="img" aria-label="Clickable map of French departments with one department highlighted"></div>
  </div>
  <div class="dept-info">
    <div class="name">Orne</div>
    <div class="kind">French Department</div>
    <p>Lorem Ipsum is simply dummy text of the printing and typesetting industry. Lorem Ipsum has been the industry's standard dummy text ever since the 1500s, when an unknown printer took a galley of type and scrambled it to make a type specimen book.</p>
    <div class="maplink"><svg width="22" height="22" viewBox="0 0 22 22"><path d="M11 2a6 6 0 0 0-6 6c0 5 6 12 6 12s6-7 6-12a6 6 0 0 0-6-6z" fill="#fff"/><circle cx="11" cy="8" r="2.2" fill="#333"/></svg>Atlas Maps</div>
  </div>
</section>

<section class="themes">
  <h2 class="section-title">Lodging By Theme</h2>
  <div class="lead">Lorem ipsum dolor sit amet, consectetur adipiscing elit.</div>
  <div class="theme-grid">
    <div class="theme-tile t1" role="img" aria-label="Photo of a seminar table">Seminar</div>
    <div class="theme-tile t2" role="img" aria-label="Photo of a beach at sunset">Peach</div>
    <div class="theme-tile t3" role="img" aria-label="Photo of a motorbike in the snow">Motorbike transplanted class</div>
    <div class="theme-tile t4" role="img" aria-label="Photo of deep water">Aquatic</div>
    <div class="theme-tile t5" role="img" aria-label="Photo of horse riding">Horse riding</div>
    <div class="theme-tile t6" role="img" aria-label="Photo of a restaurant interior">Gastronomic</div>
    <div class="theme-tile t7" role="img" aria-label="Photo of a snowy hike">Snow Nature and hike</div>
    <div class="theme-tile t8" role="img" aria-label="Photo of a sunset over water">Lorem Ipsum</div>
    <div class="theme-tile t9" role="img" aria-label="Photo of a festival crowd">Integration Weekend</div>
    <div class="theme-tile t10" role="img" aria-label="Photo of tents at a summer camp">Summer Camp</div>
    <div class="theme-tile t11" role="img" aria-label="Photo of a mountain trail">Mountain Bike</div>
    <div class="theme-tile t12" role="img" aria-label="Photo of friends around a campfire">Lorem Ipsum</div>
  </div>
</section>

<section class="ads">
  <div class="ad" style="left:175px;top:96px;width:542px;height:66px">AD</div>
  <div class="ad" style="left:175px;top:174px;width:542px;height:63px">AD</div>
  <div class="ad" style="left:779px;top:68px;width:250px;height:259px">AD</div>
</section>
<div class="divider"></div>

<section class="blog">
  <h2 class="section-title">Blog</h2>
  <article class="post" style="left:175px">
    <div class="post-photo" role="img" aria-label="Photo of a city skyline at night" style="background:linear-gradient(180deg,#1d3a6b,#c47a3a 70%,#2a2a3a)"></div>
    <h4>Lorem Ipsum is simply</h4>
    <p>Lorem Ipsum is simply dummy text of the printing and typesetting industry. Lorem Ipsum has been the industry's standard dummy text ever since the 1500s, when an unknown</p>
    <div class="post-meta"><span>● admin</span><span>◷ April 09, 2019</span><span>✉ 2 Comments</span></div>
  </article>
  <article class="post" style="left:464px">
    <div class="post-photo" role="img" aria-label="Photo of a lit bridge over a river" style="background:linear-gradient(180deg,#7f8fa8,#6a5a6a 60%,#2e3040)"></div>
    <h4>Lorem Ipsum is simply</h4>
    <p>Lorem Ipsum is simply dummy text of the printing and typesetting industry. Lorem Ipsum has been the industry's standard dummy text ever since 1...2</p>
    <div class="post-meta"><span>● admin</span><span>◷ April 09, 2019</span><span>✉ 2 Comments</span></div>
  </article>
  <article class="post" style="left:754px">
    <div class="post-photo" role="img" aria-label="Photo of a colourful village street" style="background:linear-gradient(180deg,#c6d3dc,#d69a77 50%,#7a7a6a)"></div>
    <h4>Lorem Ipsum is simply</h4>
    <p>Lorem Ipsum is simply dummy text of the printing and typesetting industry. Lorem Ipsum has been the industry's standard dummy text ever since 1...2</p>
    <div class="post-meta"><span>● admin</span><span>◷ April 09, 2019</span><span>✉ 2 Comments</span></div>
  </article>
  <span class="btn">View More</span>
</section>

<footer>
  <div class="footer">
    <div class="f-logo">lodgevista.fr</div>
    <p class="f-about">Lorem Ipsum is simply dummy text of the printing and typesetting industry. Lorem Ipsum has been the industry's standard dummy text ever since the 1500s, when an unknown</p>
    <div class="f-col" style="left:464px">
      <h5>Contact Details</h5>
      <ul>
        <li><span class="dot"></span>Lorem Ipsum is simply dummy text<br>of the printing and typesetting<br>industry.</li>
        <li style="margin-top:6px"><span class="dot"></span>+00 0000 0000</li>
      </ul>
    </div>
    <div class="f-col" style="left:695px">
      <h5>Site Link</h5>
      <ul>
        <li><span class="dot"></span>Home</li>
        <li><span class="dot"></span>Your Favorites</li>
        <li><span class="dot"></span>Blog</li>
        <li><span class="dot"></span>FAQ</li>
        <li><span class="dot"></span>Contact Us</li>
      </ul>
    </div>
    <div class="f-col" style="left:832px">
      <h5>Signup For newsletter</h5>
      <div class="f-input">E-mail</div>
      <span class="btn">Sign Up</span>
    </div>
  </div>
  <div class="copy">© copyright lodgevista.fr 2019</div>
</footer>

</body>
</html>
```